Business card design needed

We do excavation, cartage and contracting
I would quote like to have a picture of my digger as the whole back ground and the words on top. If that looks any good
Otherwise please feel free to come up with any other cool options

Cheers Marc

KLR Contracting
Excavation, Cartage, Contracting
Marcus Prewitt
www.klr-example.co.nz
021 584 067
marc@klr-example.co.nz

```html
<!DOCTYPE html>
<html lang="en">
<head>
<meta charset="utf-8">
<title>KLR Contracting – Business Card</title>
<link href="https://fonts.googleapis.com/css2?family=Arimo:ital,wght@0,400;0,700;1,700&display=swap" rel="stylesheet">
<style>
  :root {
    --green: #1f5b2c;
    --ink: #111111;
    --white: #ffffff;
    --scrub-dark: #4f5a3c;
    --gravel: #d9d0c2;
  }
  html, body {
    margin: 0;
    padding: 0;
    width: 1200px;
    height: 741px;
    overflow: hidden;
    background: #ffffff;
  }
  .card {
    position: relative;
    width: 1200px;
    height: 741px;
    overflow: hidden;
    font-family: "Arimo", Arial, sans-serif;
  }
  .card-art {
    position: absolute;
    inset: 0;
  }
  .tagline,
  .tagline-mark {
    position: absolute;
    margin: 0;
    font-weight: 700;
    line-height: 1;
    color: var(--green);
    white-space: nowrap;
  }
  .tagline {
    font-size: 37px;
    letter-spacing: 0.5px;
    text-shadow: 2px 2px 3px rgba(0,0,0,0.35);
  }
  .tagline-mark {
    left: 274px;
    top: 82px;
    font-size: 30px;
  }
  .tagline-1 { left: 349px; top: 78px; }
  .tagline-2 { left: 256px; top: 119px; }
  .tagline-3 { left: 212px; top: 158px; }
  .brand {
    position: absolute;
    left: 770px;
    top: 38px;
    width: 387px;
    height: 270px;
    display: flex;
    align-items: center;
    justify-content: center;
    gap: 22px;
  }
  .brand-square {
    width: 46px;
    height: 46px;
    background: var(--green);
  }
  .brand-name {
    font-weight: 700;
    font-size: 150px;
    line-height: 1;
    color: var(--green);
  }
  .contact {
    position: absolute;
    left: 571px;
    top: 345px;
    margin: 0;
    display: grid;
    grid-template-columns: 126px auto;
    grid-auto-rows: 60px;
    align-items: baseline;
    white-space: nowrap;
  }
  .contact dt {
    font-weight: 700;
    font-size: 25px;
    color: var(--ink);
  }
  .contact dd {
    margin: 0;
    font-weight: 400;
    font-size: 53px;
    line-height: 1;
    color: var(--ink);
  }
  .contact dd.contact-email {
    font-size: 42px;
  }
  .website {
    position: absolute;
    left: 362px;
    top: 570px;
    margin: 0;
    font-weight: 700;
    font-style: italic;
    font-size: 54px;
    line-height: 1;
    color: var(--green);
    white-space: nowrap;
  }
  .corner-mark {
    position: absolute;
    left: 52px;
    top: 630px;
    font-weight: 700;
    font-size: 46px;
    line-height: 1;
    color: var(--white);
  }
</style>
</head>
<body>
<main class="card">
  <svg class="card-art" width="1200" height="741" viewBox="0 0 1200 741">
    <defs>
      <linearGradient id="photoTone" x1="0" y1="0" x2="0.6" y2="1">
        <stop offset="0" stop-color="#b9bfb4"/>
        <stop offset="0.12" stop-color="#7d8763"/>
        <stop offset="0.45" stop-color="#4f5a3c"/>
        <stop offset="0.7" stop-color="#8e7e45"/>
        <stop offset="1" stop-color="#3e3a30"/>
      </linearGradient>
      <radialGradient id="gravelFade" cx="1" cy="1" r="0.75">
        <stop offset="0" stop-color="#d9d0c2"/>
        <stop offset="0.55" stop-color="#ebe6de"/>
        <stop offset="1" stop-color="#ffffff" stop-opacity="0"/>
      </radialGradient>
    </defs>
    <rect class="photo" x="0" y="0" width="820" height="741" fill="url(#photoTone)" role="img" aria-label="Photo of a yellow excavator bucket over scrubland with a river valley behind"/>
    <path class="white-panel" d="M760 0 H1200 V741 H528 C510 560 540 280 760 0 Z" fill="#ffffff"/>
    <rect class="gravel" x="520" y="380" width="680" height="361" fill="url(#gravelFade)" role="img" aria-label="Faded gravel ground texture"/>
    <path class="tagline-band" d="M262 58 H760 V208 H168 Z" fill="#ffffff"/>
  </svg>

  <span class="tagline-mark">KLR</span>
  <p class="tagline tagline-1">CONTRACTING.</p>
  <p class="tagline tagline-2">EXCAVATION. CARTAGE.</p>
  <p class="tagline tagline-3">CONTRACTING.</p>

  <div class="brand">
    <span class="brand-square"></span>
    <span class="brand-name">KLR</span>
  </div>

  <dl class="contact">
    <dt>Name:</dt><dd>Marcus Prewitt</dd>
    <dt>Phone:</dt><dd>021 584 067</dd>
    <dt>Email:</dt><dd class="contact-email">marc@klr-example.co.nz</dd>
  </dl>

  <p class="website">WWW.KLR-EXAMPLE.CO.NZ</p>

  <span class="corner-mark">KLR</span>
</main>
</body>
</html>
```